DM - management consultant

Business card - contemporary design

Front info
Dorian Maples

(Address not necessary)
PO Box 7386
Fernhill, OR 97999

(555) 555-0143
dm@dorianmapl.es

Twitter: dmq527
Facebook: /Dorian.Maples
Linkedin: /in/dorianmaples

Back or Front
www.dorianmaples.net
Facilitation & coaching, change management, strategic partnerships, business improvement

Target Market(s)

High tech businesses - mostly startups in Silicon Valley

Industry/Entity Type

Business

Font styles to use
Sans Serif

Colors

Designer to choose colors to be used in the design.

```html
<!DOCTYPE html>
<html lang="en">
<head>
<meta charset="utf-8">
<title>Dorian Maples – Business Card</title>
<link rel="stylesheet" href="https://fonts.googleapis.com/css2?family=Lato:wght@400;700;900&family=Roboto+Slab:wght@500&display=swap">
<style>
  :root {
    --page: #e9e7e4;
    --charcoal: #2c2c2d;
    --charcoal-soft: #3a3a3b;
    --accent: #1f9bc9;
    --paper: #ffffff;
    --ink: #3b3b3b;
    --bar: #8e8e8e;
    --chip: #5a5a5a;
    --muted: #6c6c6c;
  }
  * { margin: 0; padding: 0; box-sizing: border-box; }
  html, body { width: 794px; height: 1200px; overflow: hidden; }
  body {
    background: var(--page);
    font-family: "Lato", Arial, sans-serif;
    position: relative;
  }
  .card {
    position: absolute;
    left: 77px;
    width: 640px;
    height: 366px;
    overflow: hidden;
    box-shadow: 0 6px 18px rgba(0,0,0,.18);
  }

  /* Back side */
  .card--back { top: 150px; background: var(--charcoal); }
  .card--back .band { position: absolute; inset: 0; }
  .services {
    position: absolute;
    left: 30px; top: 100px;
    width: 560px;
    transform: rotate(-8deg);
    font-family: "Roboto Slab", Georgia, serif;
    font-weight: 500;
    font-size: 27px;
    line-height: 1.2;
    color: #fff;
  }
  .website {
    position: absolute;
    right: 34px; top: 214px;
    transform: rotate(-8deg);
    font-size: 20px;
    color: var(--accent);
  }
  .back-name {
    position: absolute;
    left: 100px; bottom: 18px;
    font-size: 46px;
    letter-spacing: 1px;
    color: var(--charcoal-soft);
    text-transform: uppercase;
  }
  .back-name b { font-weight: 900; }

  /* Front side */
  .card--front { top: 650px; background: var(--paper); }
  .name {
    position: absolute;
    left: 104px; top: 58px;
    font-size: 40px;
    font-weight: 400;
    color: var(--ink);
    text-transform: uppercase;
    letter-spacing: .5px;
  }
  .name b { color: var(--accent); font-weight: 900; }
  .contact {
    position: absolute;
    left: 104px; top: 118px;
    list-style: none;
  }
  .contact li { display: flex; align-items: center; height: 24px; margin-bottom: 5px; }
  .contact .icon {
    width: 24px; height: 24px;
    background: var(--chip);
    display: flex; align-items: center; justify-content: center;
  }
  .contact .value {
    height: 24px;
    background: var(--bar);
    color: #fff;
    font-size: 15px;
    line-height: 24px;
    padding: 0 14px 0 8px;
  }
  .social {
    position: absolute;
    left: 40px; right: 40px; top: 262px;
    display: flex; justify-content: space-between;
    list-style: none;
  }
  .social li { display: flex; align-items: center; gap: 10px; }
  .social .dot { width: 30px; height: 30px; border-radius: 50%; background: var(--chip); }
  .social .handle { font-size: 15px; line-height: 1.2; color: var(--muted); }
</style>
</head>
<body>

<section class="card card--back" aria-label="Card back">
  <svg class="band" width="640" height="366" viewBox="0 0 640 366" aria-hidden="true">
    <polygon points="0,132 640,42 640,172 0,262" fill="var(--accent)"/>
  </svg>
  <p class="services">Facilitation &amp; coaching, change management, strategic partnerships, business improvement</p>
  <p class="website">www.dorianmaples.net</p>
  <p class="back-name">Dorian <b>Maples</b></p>
</section>

<section class="card card--front" aria-label="Card front">
  <h1 class="name">Dorian <b>Maples</b></h1>
  <ul class="contact">
    <li>
      <span class="icon"><svg width="12" height="14" viewBox="0 0 12 14"><path d="M6 0a5 5 0 0 0-5 5c0 4 5 9 5 9s5-5 5-9a5 5 0 0 0-5-5zm0 7a2 2 0 1 1 0-4 2 2 0 0 1 0 4z" fill="#fff"/></svg></span>
      <span class="value">PO Box 7386, Fernhill, OR 97999</span>
    </li>
    <li>
      <span class="icon"><svg width="10" height="14" viewBox="0 0 10 14"><rect x="1" y="0" width="8" height="14" rx="1.5" fill="#fff"/><rect x="2.5" y="2" width="5" height="8" fill="var(--chip)"/></svg></span>
      <span class="value">(555) 555-0143</span>
    </li>
    <li>
      <span class="icon"><svg width="14" height="10" viewBox="0 0 14 10"><rect width="14" height="10" fill="#fff"/><path d="M0 0l7 6 7-6" fill="none" stroke="var(--chip)" stroke-width="1.4"/></svg></span>
      <span class="value">dm@dorianmapl.es</span>
    </li>
  </ul>
  <ul class="social">
    <li><span class="dot"></span><span class="handle">faceplate.com/<br>Dorian.Maples</span></li>
    <li><span class="dot"></span><span class="handle">Linkwork.com/<br>in/dorianmaples</span></li>
    <li><span class="dot"></span><span class="handle">Chirper.com/<br>dmq527</span></li>
  </ul>
</section>

</body>
</html>
```